Chestnut Farm Logo and Business Card

We need a new logo design and new business cards for a recently purchased mature Chestnut Farm in the south west of Westhaven Coast, the farm is called Willowmere Glen, We will be adding value to the chestnuts by creating a range of chestnut products based on the fact that chestnuts are a healthy, gluten free product that is suited to the vegetarian market as well as the health food market. We will be selling the products through farmers markets, restaurants, health food stores and online. The final design should communicate a healthy modern down to earth image.
Updates

Sorry, I should have given the details for the business cards.

Address is 
Willowmere Glen
PO Box 417 
Ferncombe, Westhaven Coast, 6318

Email is 
willowmere.glen@fernpost.com

Website is
www.glenhollowfoods.com

Phone number is 
(08) 9412 7730

Many thanks

We would like to see the logo separate to the business card as well if possible please?

Industry/Entity Type

Farm

Logo Text

Willowmere Glen

```html
<!DOCTYPE html>
<html lang="en">
<head>
<meta charset="utf-8">
<title>Willowmere Glen — Business Card</title>
<link rel="stylesheet" href="https://fonts.googleapis.com/css2?family=Crimson+Pro:wght@400;600&display=swap">
<style>
  :root {
    --backdrop: #e9e7e3;
    --card-white: #fbfbfa;
    --card-shade: #eeeeec;
    --leaf-green: #70a536;
    --band-text: #f3f6e8;
    --ink: #1d1d1d;
    --chestnut: #7a4320;
  }
  * { margin: 0; padding: 0; box-sizing: border-box; }
  html, body {
    width: 1200px;
    height: 900px;
    overflow: hidden;
    background: var(--backdrop);
  }
  .canvas {
    position: relative;
    width: 1200px;
    height: 900px;
    display: flex;
    align-items: center;
    justify-content: center;
  }
  .business-card {
    position: relative;
    width: 1000px;
    height: 580px;
    background: linear-gradient(160deg, var(--card-white) 40%, var(--card-shade) 100%);
    box-shadow: 0 8px 24px rgba(0, 0, 0, 0.12);
    overflow: hidden;
    font-family: "Crimson Pro", "Georgia", serif;
    font-variant-numeric: lining-nums;
  }
  .brand {
    position: absolute;
    left: 300px;
    top: 215px;
    display: flex;
    align-items: center;
    gap: 18px;
  }
  .brand-name {
    font-size: 66px;
    font-weight: 400;
    color: var(--ink);
    letter-spacing: 1px;
    line-height: 1;
    white-space: nowrap;
  }
  .brand-mark {
    width: 48px;
    height: 48px;
    border-radius: 50%;
    background: var(--chestnut);
    flex: none;
  }
  .contact-band {
    position: absolute;
    left: 0;
    right: 0;
    bottom: 0;
    height: 140px;
    background: var(--leaf-green);
    color: var(--band-text);
    font-size: 18px;
    font-weight: 600;
    line-height: 1.3;
  }
  .postal-details {
    position: absolute;
    left: 34px;
    bottom: 18px;
    font-style: normal;
  }
  .online-details {
    position: absolute;
    right: 30px;
    top: 20px;
    text-align: right;
    font-style: normal;
  }
</style>
</head>
<body>
  <main class="canvas">
    <section class="business-card" aria-label="Willowmere Glen business card">
      <div class="brand">
        <span class="brand-name">Willowmere Glen</span>
        <span class="brand-mark" aria-hidden="true"></span>
      </div>
      <footer class="contact-band">
        <address class="postal-details">
          (08) 9412 7730<br>
          PO Box 417<br>
          Ferncombe, Westhaven Coast, 6318
        </address>
        <address class="online-details">
          willowmere.glen@fernpost.com<br>
          www.glenhollowfoods.com
        </address>
      </footer>
    </section>
  </main>
</body>
</html>
```